R & M Holdings of Fairhaven, LLC
“CARE is the CORE of every HOME"
R & M Holdings of Fairhaven, LLC -
Creative Brief
Professional
Bertram Lasko
Property Manager
P.O. Box 38216 Goldsboro, NC 27534
rmholdings.office@quillpost.example

```html
<!DOCTYPE html>
<html lang="en">
<head>
<meta charset="utf-8">
<title>R &amp; M Holdings of Fairhaven, LLC – Business Cards</title>
<link rel="stylesheet" href="https://fonts.googleapis.com/css2?family=Cinzel:wght@400;600&family=Open+Sans:ital,wght@0,400;0,600;0,700;1,400&display=swap">
<style>
  :root{
    --board:#4a4a4c;
    --board-dark:#353537;
    --label:#f2f2f2;
    --paper:#ffffff;
    --ink:#1c1c1c;
    --night:#050505;
    --navy:#1b3f8f;
    --blue:#2f57b8;
    --blue-bright:#5f86e0;
    --gold:#e3a51c;
    --gold-light:#f4c340;
    --grey:#5a5a5a;
    --soft:#cfcfcf;
  }
  *{margin:0;padding:0;box-sizing:border-box}
  html,body{width:1200px;height:806px;overflow:hidden}
  body{
    background:radial-gradient(ellipse at 50% 45%,var(--board) 0%,var(--board-dark) 100%);
    font-family:"Open Sans",Arial,sans-serif;
    position:relative;
  }
  .card{
    position:absolute;width:522px;border-radius:16px;overflow:hidden;
    box-shadow:0 2px 6px rgba(0,0,0,.35);
  }
  .card--front{top:43px;height:281px}
  .card--back{top:420px;height:283px}
  .card--light{background:var(--paper)}
  .card--dark{background:var(--night)}
  .pos-a{left:48px}
  .pos-b{left:634px}

  .card-label{
    position:absolute;width:522px;text-align:center;
    font-family:"Cinzel",Georgia,serif;font-size:22px;letter-spacing:2px;
    color:var(--label);
  }
  .label-front{top:347px}
  .label-back{top:733px}

  .swoosh{position:absolute;left:0;bottom:0;width:522px;height:110px}

  .brand{position:absolute;text-align:center}
  .card--front .brand{left:14px;top:112px;width:270px}
  .card--back .brand{left:61px;top:118px;width:400px}
  .brand-name{
    font-weight:600;color:var(--navy);font-size:15px;line-height:1.25;letter-spacing:.3px;
  }
  .card--back .brand-name{font-size:21px}
  .card--dark .brand-name{color:var(--blue-bright)}
  .brand-tagline{
    margin-top:5px;font-size:8px;letter-spacing:.8px;font-weight:600;
    color:var(--gold);text-transform:uppercase;
  }
  .card--back .brand-tagline{font-size:10px;margin-top:7px}

  .contact{
    position:absolute;left:290px;top:42px;
    border-left:1px solid var(--soft);padding-left:10px;
  }
  .card--dark .contact{border-left-color:#444}
  .contact-name{font-weight:700;font-size:13px;color:var(--navy)}
  .card--dark .contact-name{color:var(--blue-bright)}
  .contact-role{font-style:italic;font-size:10px;color:var(--gold);margin-bottom:7px}
  .contact-list{list-style:none;font-size:10px;color:var(--ink)}
  .card--dark .contact-list{color:#e6e6e6}
  .contact-list li{display:flex;align-items:flex-start;gap:6px;line-height:1.4;margin-bottom:2px}
  .contact-list svg{width:9px;height:9px;flex:none;margin-top:3px;fill:var(--grey)}
  .card--dark .contact-list svg{fill:#bdbdbd}
  .icons{position:absolute;width:0;height:0}
</style>
</head>
<body>

<svg class="icons" aria-hidden="true">
  <symbol id="i-pin" viewBox="0 0 10 10"><path d="M5 0a3.5 3.5 0 0 0-3.5 3.5C1.5 6 5 10 5 10s3.5-4 3.5-6.5A3.5 3.5 0 0 0 5 0zm0 5a1.4 1.4 0 1 1 0-2.8A1.4 1.4 0 0 1 5 5z"/></symbol>
  <symbol id="i-phone" viewBox="0 0 10 10"><path d="M2 .5l1.8 2-1 1.2a6 6 0 0 0 3.5 3.5l1.2-1 2 1.8-1 1.5C5 9.5.5 5 .5 1.5z"/></symbol>
  <symbol id="i-mobile" viewBox="0 0 10 10"><path d="M3 0h4a1 1 0 0 1 1 1v8a1 1 0 0 1-1 1H3a1 1 0 0 1-1-1V1a1 1 0 0 1 1-1zm0 1.5v6h4v-6z"/></symbol>
  <symbol id="i-fax" viewBox="0 0 10 10"><path d="M2.5 0h5v3h-5zM0 3.5h10v5H8V10H2V8.5H0zm3 4v1.5h4V7.5z"/></symbol>
  <symbol id="i-mail" viewBox="0 0 10 10"><path d="M0 2h10v6H0zm1 .8v.4L5 6l4-2.8v-.4L5 5.5z"/></symbol>
</svg>

<section class="card card--front card--light pos-a">
  <div class="brand">
    <div class="brand-name">R &amp; M Holdings of Fairhaven, LL</div>
    <div class="brand-tagline">Care is the Core of every Home</div>
  </div>
  <div class="contact">
    <div class="contact-name">Bertram Lasko</div>
    <div class="contact-role">Property Manager</div>
    <ul class="contact-list">
      <li><svg><use href="#i-pin"/></svg><span>P.O. Box 38216<br>Fairhaven, NC 27534</span></li>
      <li><svg><use href="#i-phone"/></svg><span>(555) 014-2281</span></li>
      <li><svg><use href="#i-mobile"/></svg><span>(555) 014-7302</span></li>
      <li><svg><use href="#i-fax"/></svg><span>(555) 014-9916</span></li>
      <li><svg><use href="#i-mail"/></svg><span>rmholdings.office@quillpost.example</span></li>
    </ul>
  </div>
  <svg class="swoosh" viewBox="0 0 522 110" preserveAspectRatio="none" aria-hidden="true">
    <path d="M0 30 C160 100 340 40 522 58 L522 110 L0 110Z" fill="var(--navy)"/>
    <path d="M0 48 C160 110 340 60 522 74 L522 110 L0 110Z" fill="var(--blue)"/>
    <path d="M0 84 C190 114 360 58 522 36 L522 110 L0 110Z" fill="var(--gold)"/>
    <path d="M0 94 C190 120 360 72 522 52 L522 110 L0 110Z" fill="var(--gold-light)"/>
  </svg>
</section>
<p class="card-label label-front pos-a">Business Card Front A</p>

<section class="card card--front card--dark pos-b">
  <div class="brand">
    <div class="brand-name">R &amp; M Holdings of Fairhaven, LL</div>
    <div class="brand-tagline">Care is the Core of every Home</div>
  </div>
  <div class="contact">
    <div class="contact-name">Bertram Lasko</div>
    <div class="contact-role">Property Manager</div>
    <ul class="contact-list">
      <li><svg><use href="#i-pin"/></svg><span>P.O. Box 38216<br>Fairhaven, NC 27534</span></li>
      <li><svg><use href="#i-phone"/></svg><span>(555) 014-2281</span></li>
      <li><svg><use href="#i-mobile"/></svg><span>(555) 014-7302</span></li>
      <li><svg><use href="#i-fax"/></svg><span>(555) 014-9916</span></li>
      <li><svg><use href="#i-mail"/></svg><span>rmholdings.office@quillpost.example</span></li>
    </ul>
  </div>
  <svg class="swoosh" viewBox="0 0 522 110" preserveAspectRatio="none" aria-hidden="true">
    <path d="M0 22 C160 96 340 36 522 52 L522 110 L0 110Z" fill="var(--gold)"/>
    <path d="M0 38 C160 108 340 52 522 68 L522 110 L0 110Z" fill="var(--night)"/>
    <path d="M0 78 C190 112 360 58 522 38 L522 110 L0 110Z" fill="var(--blue)"/>
    <path d="M0 90 C190 120 360 74 522 56 L522 110 L0 110Z" fill="var(--navy)"/>
  </svg>
</section>
<p class="card-label label-front pos-b">Business Card Front B</p>

<section class="card card--back card--light pos-a">
  <div class="brand">
    <div class="brand-name">R &amp; M Holdings of Fairhaven, LL</div>
    <div class="brand-tagline">Care is the Core of every Home</div>
  </div>
</section>
<p class="card-label label-back pos-a">Business Card Back A</p>

<section class="card card--back card--dark pos-b">
  <div class="brand">
    <div class="brand-name">R &amp; M Holdings of Fairhaven, LL</div>
    <div class="brand-tagline">Care is the Core of every Home</div>
  </div>
</section>
<p class="card-label label-back pos-b">Business Card Back B</p>

</body>
</html>
```